Upscale business cards needed for family business

We need professional business cards created for several family members. We are a family business holding company. We would like these relatively simple and straightforward, but also with a unique element to set them apart. Probably stick with neutral and simple colors - white, grey etc. We need space for the traditional elements, including name, title, address, email/phone number. And we will be creating several from this template so it needs to be template that is easy to switch information in and out of.

Industry/Entity Type

Business

Contact Information for Business Card

Please include the attached Dunmore Ventures logo.

Requirements
Must have
• The attached Dunmore Ventures logo.

```html
<!DOCTYPE html>
<html lang="en">
<head>
<meta charset="UTF-8">
<title>Dunmore Ventures – Business Card</title>
<link href="https://fonts.googleapis.com/css2?family=Cinzel:wght@400;600&family=Questrial&display=swap" rel="stylesheet">
<style>
  :root {
    --page-bg: #e9e6e0;
    --card-black: #0b0b0b;
    --card-sheen: #2a2a2a;
    --gold: #d9c27a;
    --gold-deep: #b9993f;
    --white: #f4f4f2;
    --line: #e6e6e6;
  }
  * { margin: 0; padding: 0; box-sizing: border-box; }
  html, body {
    width: 1200px; height: 1022px; overflow: hidden;
    background: var(--page-bg);
  }
  .stage {
    width: 1200px; height: 1022px;
    display: flex; align-items: center; justify-content: center;
  }
  .card {
    position: relative;
    width: 900px; height: 514px;
    border-radius: 14px;
    background: linear-gradient(120deg, var(--card-black) 0%, var(--card-sheen) 45%, var(--card-black) 75%);
    border-right: 14px solid var(--gold);
    box-shadow: 0 18px 40px rgba(0,0,0,.25);
    overflow: hidden;
    font-family: "Questrial", sans-serif;
    color: var(--white);
  }
  .brand {
    position: absolute; left: 70px; top: 84px;
    display: flex; align-items: center; gap: 18px;
  }
  .brand-dot {
    width: 44px; height: 44px; border-radius: 50%;
    background: var(--gold); flex: none;
  }
  .brand-text { display: flex; flex-direction: column; }
  .brand-name {
    font-family: "Cinzel", serif; font-weight: 400;
    font-size: 33px; letter-spacing: 1px; color: var(--white);
    white-space: nowrap;
    padding-bottom: 6px; border-bottom: 2px solid var(--gold-deep);
  }
  .brand-suffix {
    font-family: "Cinzel", serif; font-size: 15px;
    color: var(--white); align-self: center; margin-top: 6px; letter-spacing: 2px;
  }
  .person {
    position: absolute; right: 60px; top: 70px;
    display: flex; flex-direction: column; align-items: flex-end;
  }
  .person-name {
    font-family: "Cinzel", serif; font-weight: 400;
    font-size: 30px; color: var(--gold); white-space: nowrap;
    padding-bottom: 8px; border-bottom: 2px solid var(--line);
  }
  .person-title { font-size: 20px; margin-top: 8px; }
  .address {
    position: absolute; right: 60px; top: 210px;
    text-align: right; font-size: 21px; line-height: 1.6;
  }
  .divider {
    position: absolute; left: 70px; right: 60px; top: 320px;
    height: 2px; background: var(--line);
  }
  .contacts {
    position: absolute; left: 70px; top: 345px;
    list-style: none; font-size: 22px; line-height: 1.55;
  }
  .contacts li { display: flex; align-items: center; gap: 16px; }
  .contacts svg { width: 16px; height: 16px; flex: none; }
  .web-domain { color: var(--gold); font-weight: 600; }
</style>
</head>
<body>
<main class="stage">
  <article class="card">
    <div class="brand">
      <span class="brand-dot"></span>
      <div class="brand-text">
        <span class="brand-name">Dunmore Ventures</span>
        <span class="brand-suffix">Inc</span>
      </div>
    </div>

    <div class="person">
      <h1 class="person-name">Marten Ellison</h1>
      <p class="person-title">Director</p>
    </div>

    <p class="address">Ostergasse 7/1/2106<br>A - 1100, Wien</p>

    <div class="divider"></div>

    <ul class="contacts">
      <li>
        <svg viewBox="0 0 16 16" aria-hidden="true"><path d="M3 1h3l1.5 4-2 1.2a9 9 0 0 0 4.3 4.3L11 8.5l4 1.5v3a2 2 0 0 1-2 2A12 12 0 0 1 1 3a2 2 0 0 1 2-2z" fill="var(--gold)"/></svg>
        +330 2815-4093
      </li>
      <li>
        <svg viewBox="0 0 16 16" aria-hidden="true"><rect x="1" y="3" width="14" height="10" fill="none" stroke="var(--gold)" stroke-width="1.5"/><path d="M1 3l7 6 7-6" fill="none" stroke="var(--gold)" stroke-width="1.5"/></svg>
        info@dunmoreventures.com
      </li>
      <li>
        <svg viewBox="0 0 16 16" aria-hidden="true"><circle cx="8" cy="8" r="6.5" fill="none" stroke="var(--gold)" stroke-width="1.4"/><ellipse cx="8" cy="8" rx="3" ry="6.5" fill="none" stroke="var(--gold)" stroke-width="1.2"/><path d="M1.5 8h13" stroke="var(--gold)" stroke-width="1.2"/></svg>
        <span>www.<span class="web-domain">dunmoreventures</span>.com</span>
      </li>
    </ul>
  </article>
</main>
</body>
</html>
```